Saffron Ember

we need a flyer design. for an A4 sheet folded into 3 layers/pages.
for an Indian fast food take away. Please use up to date UK standard menu design.
Any more info needed can contact us anytime by email.
word document of item for the flyer attached.

Target Market(s)

Indian Food lovers

Industry/Entity Type

Indian Restaurant

Font styles to use
Decorative
Script

Colors
cbe087
abd036
fbf289
f37022

Requirements
Must have
• Can you please bleed the menu so that I can show it to the printer guy
Nice to have
• modern menu

```html
<!DOCTYPE html>
<html lang="en">
<head>
<meta charset="utf-8">
<title>Saffron Ember – Takeaway Menu</title>
<link href="https://fonts.googleapis.com/css2?family=Zilla+Slab:wght@300;400;600;700&family=Raleway:wght@400;500;600&display=swap" rel="stylesheet">
<style>
:root{
  --brown:#4a2a22;
  --brown-deep:#3a1f19;
  --brown-mid:#6a3f33;
  --orange:#f37022;
  --red:#e5392a;
  --green:#8cc63f;
  --ink:#2b2420;
  --grey-text:#6d6661;
  --card-top:#ffffff;
  --card-bottom:#e6e6e6;
  --footer:#aaa49f;
}
*{box-sizing:border-box;margin:0;padding:0}
html,body{width:1200px;height:848px;overflow:hidden;background:#fff}
body{font-family:"Raleway",sans-serif;color:var(--ink)}
.flyer{position:relative;width:1200px;height:848px;overflow:hidden;background:#fff}
.backdrop{position:absolute;inset:0}
.abs{position:absolute}
.panel-title{font-family:"Zilla Slab",serif;font-weight:600;color:#fff;font-size:27px;letter-spacing:.5px}
.size-note{left:256px;top:194px;width:122px;text-align:right;font-size:14px;color:var(--ink)}

.card{position:absolute;left:16px;width:368px;border-radius:12px;
  background:linear-gradient(180deg,var(--card-top),var(--card-bottom));
  box-shadow:0 1px 3px rgba(0,0,0,.08)}
.pizza-card{top:224px;height:350px}
.drinks-card{top:668px;height:156px}

.item{position:absolute;left:26px;right:29px}
.item-head{display:flex;align-items:baseline;font-family:"Zilla Slab",serif;font-size:17px}
.item-num{color:var(--orange);font-weight:600;width:25px}
.item-name{color:var(--red);font-weight:700}
.dots{flex:1;border-bottom:1px dotted var(--ink);margin:0 4px 0 6px;transform:translateY(-4px)}
.price{color:var(--orange);font-family:"Raleway",sans-serif;font-size:15px}
.item-desc{font-size:14px;line-height:17px;padding-left:21px;margin-top:3px;text-align:justify}
.tag{display:inline-block;width:11px;height:11px;border-radius:50%;background:var(--orange);
  color:#fff;font-size:8px;line-height:11px;text-align:center;font-family:"Raleway",sans-serif;margin-left:5px;vertical-align:1px}
.tag.grey{background:#c9c6c3}
.drink .item-name{font-size:17px}
.drink .size{font-family:"Raleway",sans-serif;font-size:13px;color:var(--ink);margin-left:5px}

.set-meal{position:absolute;left:434px;width:286px}
.set-title{font-family:"Zilla Slab",serif;font-weight:700;color:var(--green);font-size:17px;line-height:20px}
.set-title .dots{border-color:var(--green)}
.set-title .price{color:var(--green)}
.set-list{list-style:none;margin-top:6px}
.set-list li{font-size:14px;line-height:20.8px;padding-left:12px;position:relative}
.set-list li::before{content:"";position:absolute;left:1px;top:9px;width:4px;height:4px;border-radius:50%;background:var(--ink)}

.info-box{position:absolute;left:402px;top:594px;width:394px;height:254px;
  background:linear-gradient(180deg,var(--brown-deep),var(--brown-mid));color:#f1ebe7;padding:20px 17px 0 18px}
.info-box p{font-size:12.2px;line-height:14.4px;letter-spacing:.25px;text-align:justify}
.allergen-title{font-size:14px;margin-top:5px}
.allergen-cols{display:flex;margin-top:10px;font-size:11.8px;line-height:17px}
.allergen-cols ol{list-style:none}
.allergen-cols ol:nth-child(1){width:117px}
.allergen-cols ol:nth-child(2){width:126px}

.web{right:16px;top:12px;color:#fff;font-family:"Zilla Slab",serif;font-size:13px}
.hero-word{font-family:"Zilla Slab",serif}
.hero-authentic{left:822px;top:30px;color:var(--orange);font-weight:700;font-size:24px}
.hero-indian{left:820px;top:54px;color:#fff;font-weight:300;font-size:46px;letter-spacing:1px}
.hero-food{left:822px;top:102px;color:var(--green);font-weight:700;font-size:24px}

.brand{left:796px;width:404px;text-align:center}
.brand-name{top:576px;font-family:"Zilla Slab",serif;font-weight:700;font-size:42px;color:var(--brown-deep)}
.brand-tag{top:640px;font-family:"Zilla Slab",serif;font-weight:700;font-size:23px;color:var(--ink)}
.brand-tag .k{color:var(--green)} .brand-tag .p{color:var(--orange)} .brand-tag .c{color:var(--red)}
.address{top:686px;font-family:"Zilla Slab",serif;font-size:15px;color:var(--grey-text)}
.rule{top:709px;left:874px;width:248px;border-top:1px dotted var(--grey-text)}
.hours{top:714px;font-size:14px;line-height:18px;color:var(--grey-text)}
.hours b{font-family:"Zilla Slab",serif;font-weight:700;font-size:15px}
.contact-band{left:796px;top:774px;width:404px;height:74px;background:var(--footer);
  color:var(--ink);text-align:right;padding:7px 16px 0 0;font-size:14px;line-height:18.5px}
.contact-band b{font-weight:600}
.contact-band .big{font-size:16px}
</style>
</head>
<body>
<div class="flyer">

  <svg class="backdrop" width="1200" height="848" viewBox="0 0 1200 848" aria-hidden="true">
    <defs>
      <linearGradient id="pizzaTone" x1="0" y1="0" x2="1" y2="1">
        <stop offset="0" stop-color="#e9d2b0"/><stop offset=".5" stop-color="#d8583e"/><stop offset="1" stop-color="#f2e6d6"/>
      </linearGradient>
      <linearGradient id="mealTone" x1="0" y1="0" x2="1" y2="1">
        <stop offset="0" stop-color="#4b4644"/><stop offset=".45" stop-color="#d9862f"/><stop offset="1" stop-color="#3c3634"/>
      </linearGradient>
      <radialGradient id="spiceTone" cx=".55" cy=".5" r=".6">
        <stop offset="0" stop-color="#c9a27a"/><stop offset=".55" stop-color="#b8452b"/><stop offset="1" stop-color="#ffffff" stop-opacity="0"/>
      </radialGradient>
    </defs>
    <polygon points="0,132 470,0 400,0 400,168 0,226" fill="url(#pizzaTone)" role="img" aria-label="Photo of a margherita pizza with tomatoes and basil"/>
    <polygon points="0,0 480,0 0,104" fill="var(--brown)"/>
    <polygon points="0,104 480,0 500,0 0,132" fill="var(--orange)"/>
    <polygon points="400,0 470,0 796,100 796,255 400,162" fill="url(#mealTone)" role="img" aria-label="Photo of a curry thali with chillies and tomatoes"/>
    <polygon points="455,0 796,0 796,84" fill="var(--brown)"/>
    <polygon points="455,0 478,0 796,102 796,84" fill="var(--green)"/>
    <polygon points="0,576 240,618 0,680" fill="var(--brown)"/>
    <polygon points="0,680 240,618 0,694" fill="var(--red)"/>
    <polygon points="796,244 1200,40 1200,420 1120,520 920,505 796,470" fill="url(#spiceTone)" role="img" aria-label="Photo of fresh ginger, chillies and ground spices"/>
    <polygon points="796,0 1200,0 1200,24 796,228" fill="var(--brown)"/>
    <polygon points="796,228 1200,24 1200,40 796,244" fill="var(--green)"/>
    <g font-family="Raleway, sans-serif" font-size="9" fill="#fff" text-anchor="middle">
      <g fill="var(--red)">
        <circle cx="197" cy="167" r="6.5"/><circle cx="213" cy="167" r="6.5"/><circle cx="229" cy="167" r="6.5"/><circle cx="245" cy="167" r="6.5"/><circle cx="261" cy="167" r="6.5"/><circle cx="277" cy="167" r="6.5"/><circle cx="293" cy="167" r="6.5"/><circle cx="309" cy="167" r="6.5"/><circle cx="325" cy="167" r="6.5"/><circle cx="341" cy="167" r="6.5"/>
      </g>
      <text x="197" y="170">1</text><text x="213" y="170">2</text><text x="229" y="170">3</text><text x="245" y="170">4</text><text x="261" y="170">5</text><text x="277" y="170">6</text><text x="293" y="170">7</text><text x="309" y="170">8</text><text x="325" y="170">9</text><text x="341" y="170">10</text>
    </g>
  </svg>

  <!-- Pizza panel -->
  <div class="abs panel-title" style="left:25px;top:22px">Pizza</div>
  <div class="abs size-note">................(10″/12″)</div>

  <section class="card pizza-card" aria-label="Pizza menu">
    <div class="item" style="top:12px;left:10px">
      <div class="item-head"><span class="item-num">1.</span><span class="item-name">Margarita</span><span class="tag">7</span><span class="dots"></span><span class="price">£ 4.50/5.00</span></div>
      <div class="item-desc">Tomato and mozzarella cheese</div>
    </div>
    <div class="item" style="top:68px;left:10px">
      <div class="item-head"><span class="item-num">2.</span><span class="item-name">Mexican</span><span class="tag">7</span><span class="dots"></span><span class="price">£ 6.00/7.00</span></div>
      <div class="item-desc">Cheese, pepperoni, peppers, onions, jalapenos and chilli</div>
    </div>
    <div class="item" style="top:140px;left:10px">
      <div class="item-head"><span class="item-num">3.</span><span class="item-name">Hawaiian</span><span class="tag">7</span><span class="dots"></span><span class="price">£ 5.00/6.00</span></div>
      <div class="item-desc">Ham, cheese and pineapple</div>
    </div>
    <div class="item" style="top:196px;left:10px">
      <div class="item-head"><span class="item-num">4.</span><span class="item-name">Milano</span><span class="tag">7</span><span class="dots"></span><span class="price">£ 6.00/7.00</span></div>
      <div class="item-desc">Ham, chicken, cheese and sweetcorn, peppers</div>
    </div>
    <div class="item" style="top:252px;left:10px">
      <div class="item-head"><span class="item-num">5.</span><span class="item-name">Vegetarian</span><span class="tag">7</span><span class="dots"></span><span class="price">£ 5.00/6.00</span></div>
      <div class="item-desc">Tomato, Cheese, mushroom, onion, pepper, sweetcorn</div>
    </div>
    <div class="item" style="top:321px;left:10px">
      <div class="item-head"><span class="item-num">6.</span><span class="item-name">Garlic Bread</span><span class="dots"></span><span class="price">£ 3.50/4.50</span></div>
    </div>
  </section>

  <div class="abs panel-title" style="left:25px;top:602px;font-size:28px">Soft Drinks</div>

  <section class="card drinks-card" aria-label="Soft drinks">
    <div class="item drink" style="top:22px;left:12px">
      <div class="item-head"><span class="item-num">1.</span><span class="item-name">Lemonade</span><span class="size">330 ml can</span><span class="dots"></span><span class="price">£ 1.00</span></div>
    </div>
    <div class="item drink" style="top:57px;left:12px">
      <div class="item-head"><span class="item-num">2.</span><span class="item-name">Orange Soda</span><span class="size">330 ml can</span><span class="dots"></span><span class="price">£ 1.00</span></div>
    </div>
    <div class="item drink" style="top:88px;left:12px">
      <div class="item-head"><span class="item-num">3.</span><span class="item-name">Cola</span><span class="size">330 ml can</span><span class="dots"></span><span class="price">£ 1.00</span></div>
    </div>
    <div class="item drink" style="top:123px;left:12px">
      <div class="item-head"><span class="item-num">4.</span><span class="item-name">Diet Cola</span><span class="size">330 ml can</span><span class="dots"></span><span class="price">£ 1.00</span></div>
    </div>
  </section>

  <!-- Meal panel -->
  <div class="abs panel-title" style="left:697px;top:14px">Meal</div>

  <section class="set-meal" style="top:216px" aria-label="Set meal for one">
    <div class="set-title">Set Meal B for 1 -</div>
    <div class="set-title" style="display:flex;align-items:baseline">Non-Vegetarian<span class="dots"></span><span class="price">£ 16.00</span></div>
    <ul class="set-list">
      <li>Chicken tikka starter <span class="tag grey">7</span></li>
      <li>Chicken tikka masala <span class="tag grey">7</span></li>
      <li>Pilau Rice</li>
      <li>Plain Naan <span class="tag grey">8</span></li>
      <li>Popadoms and spiced onions</li>
      <li>Choice of soft drink</li>
    </ul>
  </section>

  <section class="set-meal" style="top:399px" aria-label="Set meal for two">
    <div class="set-title" style="display:flex;align-items:baseline">Set Meal B for 2<span class="dots"></span><span class="price">£ 25.00</span></div>
    <ul class="set-list">
      <li>Onion bhaji</li>
      <li>Chicken tikka starter <span class="tag grey">7</span></li>
      <li>Chicken tikka masala <span class="tag grey">7</span></li>
      <li>Lamb Roganjosh</li>
      <li>2 × Pilau rice</li>
      <li>Plain Naan <span class="tag grey">8</span></li>
      <li>Poppadum with spiced onion</li>
      <li>2 soft drinks</li>
    </ul>
  </section>

  <section class="info-box" aria-label="Allergen information">
    <p>We cook all our meals to order, and each main course is cooked separately, so our pots and pans get used throughout service. Our equipment is washed thoroughly between each preparation, but we cannot guarantee some allergens will not be present. If you are extremely susceptible to nuts for example, please inform us when ordering. No MSG is used in any of our cooking.</p>
    <div class="allergen-title">Allergens :</div>
    <div class="allergen-cols">
      <ol><li>1. Eggs</li><li>2. Nuts</li><li>3. Mustard</li><li>4. Crustaceans</li><li>5. Soya</li></ol>
      <ol><li>6. Fish</li><li>7. Milk / Yoghurt</li><li>8. Gluten</li><li>9. Sesame Seeds</li><li>10. Celery</li></ol>
      <ol><li>11. Lupin</li><li>12. Peanuts</li><li>13. Molluscs</li><li>14. Sulpher dioxide</li></ol>
    </div>
  </section>

  <!-- Front panel -->
  <div class="abs web">www.saffronember.co.uk</div>
  <div class="abs hero-word hero-authentic">Authentic</div>
  <div class="abs hero-word hero-indian">INDIAN</div>
  <div class="abs hero-word hero-food">Food</div>

  <div class="abs brand brand-name">Saffron Ember</div>
  <div class="abs brand brand-tag"><span class="k">Kebab</span> – <span class="p">Pizza</span> – <span class="c">Curry</span></div>
  <div class="abs brand address">14, Harrow Lane, Kilbrook, BT70 2QR</div>
  <div class="abs rule"></div>
  <div class="abs brand hours">Opening hours :<br>WED - MON &nbsp;|&nbsp; <b>5pm – 10.30pm</b><br>Closed : Tuesday</div>

  <div class="abs contact-band">
    Contact <b>saffronember.orders@mail.com</b> or<br>
    call us at <b>0288.555.0193</b><br>
    <span class="big">to set up custom catering</span>
  </div>

</div>
</body>
</html>
```